Energieberater sucht Flyer-Design
Zielgruppe
Ich bin Energieberater, habe mich vor kurzem selbstständig gemacht und möchte nun meine Bekanntheit steigern. Meine Zielgruppe sind Immobilieneigentümer sowie Immobiliensuchende, welchen ich eine fundierte Energieberatung mit Sanierungskonzepten sowie die Erstellung von Energieausweisen bieten kann.
Aufgabenstellung
Ich benötige einen Flyer, welchen ich regional verteilen möchte. Der Flyer soll quadratisch (148 x 148) erstellt werden.
Der Flyer sollte mein Logo, meine Kontaktdaten, die unten aufgeführten Dienstleistungen sowie einen Gutschein enthalten und insbesondere der Bekanntheits-/Imagesteigerung dienen.
Vorhandene Punkte sollen sein:
- Erstellung von Energieausweisen für Vermietung und Verkauf
- Energieberatung
- Sanierungs- und Modernisierungskonzepte
- Fördermittelberatung
Der Flyer soll die Möglichkeit bieten, am Rand abgeschnitten zu werden. Dort soll ein Gutschein aufgeführt werden mit 25 € Rabatt für einen Energieausweis.
Meine Kontaktdaten können Sie der angehängten Visitenkarte entnehmen.

```html
<!DOCTYPE html>
<html lang="de">
<head>
<meta charset="utf-8">
<title>Flyer Energieberatung Jonas Wendel</title>
<link href="https://fonts.googleapis.com/css2?family=Saira+Semi+Condensed:wght@400;500;600&family=Exo+2:wght@600;700;800&display=swap" rel="stylesheet">
<style>
  :root {
    --teal: #1e7896;
    --teal-dark: #19667f;
    --slate: #555759;
    --grey-bg: #c8c8c8;
    --white: #ffffff;
    --text-grey: #6b6b6b;
    --olive: #a8b03a;
    --yellow: #e8c51e;
    --orange: #ec7a23;
    --red: #d8252a;
    --skin: #e9c2a8;
    --skin-light: #f5e1d3;
  }
  * { box-sizing: border-box; margin: 0; padding: 0; }
  html, body { width: 1200px; height: 623px; overflow: hidden; }
  body {
    background: var(--grey-bg);
    position: relative;
    font-family: "Saira Semi Condensed", sans-serif;
  }
  .flyer-side {
    position: absolute;
    top: 39px;
    width: 535px;
    height: 535px;
    background: var(--white);
    box-shadow: 0 3px 8px rgba(0,0,0,.28);
    overflow: hidden;
  }
  .front { left: 42px; }
  .back { left: 619px; }

  /* Front */
  .brand {
    position: absolute;
    left: 52px; top: 52px;
    display: flex; align-items: center; gap: 14px;
  }
  .brand-square { width: 26px; height: 26px; background: var(--teal); }
  .brand-name {
    font-family: "Exo 2", sans-serif;
    font-weight: 700;
    font-size: 25px;
    color: var(--teal);
    letter-spacing: .5px;
  }
  .front-band {
    position: absolute; left: 0; top: 159px;
    width: 100%; height: 13px; background: var(--teal);
  }
  .front-photo {
    position: absolute; left: 180px; top: 172px;
    width: 355px; height: 363px;
    background:
      linear-gradient(90deg, var(--white) 0%, rgba(255,255,255,0) 45%),
      radial-gradient(ellipse at 62% 55%, var(--skin) 0%, var(--skin-light) 55%, var(--white) 100%);
  }
  .services {
    position: absolute; left: 30px; top: 0;
    list-style: none;
  }
  .services li {
    position: absolute; left: 0;
    width: 320px;
    padding-left: 19px;
    font-weight: 500;
    font-size: 20px;
    line-height: 21.6px;
    color: var(--teal);
  }
  .services li::before {
    content: ""; position: absolute; left: 0; top: 6px;
    width: 9px; height: 9px; background: var(--c);
  }
  .svc-1 { top: 244px; --c: var(--olive); }
  .svc-2 { top: 338px; --c: var(--yellow); }
  .svc-3 { top: 390px; --c: var(--orange); }
  .svc-4 { top: 464px; --c: var(--red); }

  /* Back */
  .info-panel {
    position: absolute; left: 0; top: 0;
    width: 313px; height: 248px;
    background: var(--teal);
    padding: 27px 20px 0 29px;
    color: var(--white);
    font-size: 12.6px; line-height: 14px;
  }
  .info-panel p + p { margin-top: 28px; }
  .contact-panel {
    position: absolute; left: 317px; top: 0;
    width: 218px; height: 248px;
    background: var(--slate);
    color: var(--white);
  }
  .contact-name {
    position: absolute; left: 27px; top: 101px;
    font-weight: 600; font-size: 18px; line-height: 17px;
  }
  .contact-list {
    position: absolute; left: 27px; top: 150px;
    list-style: none; font-size: 9.6px; line-height: 14px;
  }
  .contact-list li { display: flex; gap: 4px; align-items: flex-start; }
  .contact-list svg { width: 7px; height: 8px; margin-top: 3px; flex: none; fill: var(--white); }
  .contact-list .spacer { height: 14px; }
  .house-visual {
    position: absolute; left: 205px; top: 252px;
    width: 330px; height: 242px;
    background: linear-gradient(160deg, #b88a5a 0%, #9a9a9a 40%, #e6e8ea 70%, #f6f6f6 100%);
    opacity: .85;
  }
  .voucher {
    position: absolute; left: 52px; top: 352px;
    width: 178px; height: 100px;
    transform: rotate(-14deg);
    border-radius: 8px 20px 20px 8px;
    overflow: hidden;
    background: var(--slate);
    color: var(--white);
  }
  .voucher-hole {
    position: absolute; right: 12px; top: 36px;
    width: 10px; height: 10px; border-radius: 50%; background: var(--white);
  }
  .voucher-amount {
    position: absolute; left: 30px; top: 4px;
    font-family: "Exo 2", sans-serif; font-weight: 800;
    font-size: 33px; line-height: 32px;
  }
  .voucher-amount span { display: block; font-size: 25px; line-height: 24px; }
  .voucher-note {
    position: absolute; left: 0; bottom: 0; width: 100%; height: 36px;
    background: var(--teal);
    padding: 3px 0 0 30px;
    font-family: "Exo 2", sans-serif; font-weight: 700;
    font-size: 13px; line-height: 14px;
  }
  .web-band {
    position: absolute; left: 0; top: 494px;
    width: 100%; height: 41px;
    background: var(--teal);
    color: var(--white);
    font-family: "Exo 2", sans-serif; font-weight: 700;
    font-size: 19px;
    display: flex; align-items: center; justify-content: center;
    padding-left: 20px;
  }
</style>
</head>
<body>

<section class="flyer-side front">
  <div class="brand">
    <span class="brand-square"></span>
    <span class="brand-name">Energieberatung Jonas Wendel</span>
  </div>
  <div class="front-band"></div>
  <div class="front-photo" role="img" aria-label="Foto: Hände umschließen ein weißes Papierhaus mit Energieeffizienzskala A bis G"></div>
  <ul class="services">
    <li class="svc-1">Erstellung von<br>Energieausweisen<br>für Vermietung und Verkauf</li>
    <li class="svc-2">Energieberatung</li>
    <li class="svc-3">Sanierungs- und<br>Modernisierungskonzepte</li>
    <li class="svc-4">Fördermittelberatung</li>
  </ul>
</section>

<section class="flyer-side back">
  <div class="info-panel">
    <p>Wir unterstützen Sie bei der Erstellung eines Energieausweises, nehmen eine Begutachtung der Gebäudesubstanz vor, zeigen den energetischen IST-Zustand anhand der Energieeffizienzklassen auf und leiten Modernisierungs -empfehlungen zur Verbesserung der Energieeffizienz ab.</p>
    <p>Als Käufer erhalten Sie mit Übergabe des Energieausweises einen Wegweiser, um die Kosten der anstehenden Modernisierung einschätzen zu können und einen Überblick über den baulichen Zustand der Immobilie zu erhalten.</p>
  </div>
  <div class="contact-panel">
    <div class="contact-name">Energieberatung<br>Jonas Wendel</div>
    <ul class="contact-list">
      <li><svg viewBox="0 0 10 12"><path d="M5 0a4 4 0 0 0-4 4c0 3 4 8 4 8s4-5 4-8a4 4 0 0 0-4-4zm0 5.5A1.5 1.5 0 1 1 5 2.5a1.5 1.5 0 0 1 0 3z"/></svg><span>Lindenweg 14<br>35390 Talheim</span></li>
      <li class="spacer"></li>
      <li><svg viewBox="0 0 10 10"><path d="M2 0l2 2.5-1 1.2c.6 1.3 1.7 2.4 3 3l1.2-1L10 8l-1.2 2C4.5 10 0 5.5 0 1.2z"/></svg><span>+49 0151 55501234</span></li>
      <li><svg viewBox="0 0 10 8"><path d="M0 0h10v1L5 4 0 1zM0 2l5 3 5-3v6H0z"/></svg><span>info@energieberatung-wendel.com</span></li>
    </ul>
  </div>
  <div class="house-visual" role="img" aria-label="Illustration: Haus im Rohbau mit offenem Dachstuhl auf Bauplänen"></div>
  <div class="voucher">
    <span class="voucher-hole"></span>
    <div class="voucher-amount">25 €<span>RABATT</span></div>
    <div class="voucher-note">für einen<br>Energieausweis</div>
  </div>
  <div class="web-band">www.energieberatung-wendel.com</div>
</section>

</body>
</html>
```